Landscape Supplier and Excavation company needing a website revamp.

We need a web design for our company based out of northern Virginia. We make and deliver topsoil, mulch, and compost. We are also an excavation company. We provide a wide variety of excavation services, from residential to large commercial projects. We specialize in land clearing and building site preparation. We would like a site that looks very professional and makes us look like a large company. We've been in business since 1994 and have never had a really nice website. Our current website it www.harrowfieldloam.com and www.pvrqx.com for references. I like the information on the pages but would like something more professional looking. Doesn't HAVE to be 4 different pages, but I would like a contact form, our services, and our products/ pricing listed. We are properly licensed and insured and would like this included somewhere on the site.

Target Market(s)

Landscapers, Home Owners, Commercial

Industry/Entity Type

Excavation and Landscape Products Supplier

Number of Pages Required

4 page

Colors

Designer to choose colors to be used in the design.

Requirements
Must have
• Professional Look and Feel

```html
<!DOCTYPE html>
<html lang="en">
<head>
<meta charset="utf-8">
<title>Harrowfield Loam &amp; Excavation</title>
<link href="https://fonts.googleapis.com/css2?family=Roboto:wght@300;400;500;700&family=Open+Sans:ital,wght@0,400;0,600;1,600&family=Russo+One&display=swap" rel="stylesheet">
<style>
:root{
  --red:#c8202a;
  --ink:#2b2b2b;
  --muted:#555;
  --paper:#f3f3f3;
  --dark:#2a2827;
  --footer:#2f2f2f;
  --white:#fff;
}
*{box-sizing:border-box;margin:0;padding:0}
html,body{width:1200px;height:4175px;overflow:hidden}
body{position:relative;background:var(--paper);font-family:"Open Sans",sans-serif;color:var(--ink)}
.abs{position:absolute}
.btn{position:absolute;display:flex;align-items:center;justify-content:center;background:var(--red);color:var(--white);border-radius:20px;font-size:13px;font-family:"Open Sans",sans-serif}
.photo{position:absolute;border-radius:50%}

/* header */
.site-header{position:absolute;left:0;top:0;width:1200px;height:143px;background:var(--paper)}
.brand{position:absolute;left:73px;top:36px;display:flex;align-items:center;gap:12px}
.brand-mark{width:18px;height:18px;background:var(--red)}
.brand-name{font-family:"Roboto",sans-serif;font-weight:700;font-size:24px;line-height:1.1;color:var(--ink);letter-spacing:1px}
.header-phone{position:absolute;left:802px;top:38px;display:flex;align-items:center;gap:8px;font-family:"Roboto",sans-serif;font-size:18px}
.phone-dot{width:32px;height:32px;border-radius:50%;background:var(--red);display:flex;align-items:center;justify-content:center}
.quote-btn{left:982px;top:35px;width:143px;height:34px;font-size:14px}
.main-nav{position:absolute;top:91px;right:75px;display:flex;gap:33px;font-family:"Roboto",sans-serif;font-size:13px;letter-spacing:2.2px;color:var(--ink)}
.main-nav .active{color:var(--red);border-bottom:2px solid var(--red);padding-bottom:8px}

/* hero */
.hero{position:absolute;left:0;top:143px;width:1200px;height:694px;background:linear-gradient(180deg,#6d7277 0%,#5a5a52 22%,#6b5a45 45%,#5b4634 75%,#4b3a2c 100%)}
.hero-title{position:absolute;left:0;top:305px;width:1200px;text-align:center;font-family:"Russo One",sans-serif;font-size:38px;line-height:50px;color:var(--white);text-shadow:0 2px 6px rgba(0,0,0,.6)}
.slide-dots{position:absolute;left:1140px;top:332px;display:flex;flex-direction:column;gap:7px}
.slide-dots span{width:7px;height:7px;border-radius:50%;background:rgba(255,255,255,.55)}
.slide-dots span.on{background:var(--white)}
.slide-num{position:absolute;left:1153px;top:340px;color:var(--white);font-family:"Roboto",sans-serif;font-size:14px}

/* about */
.section-title{position:absolute;left:0;width:1200px;text-align:center;font-family:"Roboto",sans-serif;font-weight:400;color:var(--ink)}
.about-title{top:908px;font-size:34px}
.title-rule{position:absolute;left:575px;top:972px;width:46px;height:2px;background:var(--red)}
.about-photo{left:146px;top:952px;width:418px;height:418px;background:radial-gradient(circle at 50% 30%,#c8cdd2 0%,#a98873 45%,#a4492f 75%,#8c3f2c 100%)}
.about-text{position:absolute;left:618px;top:1012px;width:500px;font-size:12.6px;line-height:22px;color:var(--ink)}
.about-text p{margin-bottom:22px}
.about-text p+p{margin-top:-2px}
.about-btn{left:621px;top:1298px;width:154px;height:39px}

/* services */
.services{position:absolute;left:0;top:1465px;width:1200px;height:1228px;background:var(--dark)}
.services-title{top:70px;font-size:36px;color:var(--white)}
.service-card{position:absolute;width:366px;text-align:center;color:var(--white)}
.service-card.featured{background:var(--paper);color:var(--ink);border-radius:4px;box-shadow:0 4px 14px rgba(0,0,0,.4)}
.service-clip{position:absolute;left:27px;width:311px;height:275px;overflow:hidden;border-radius:156px 156px 0 0}
.service-clip div{width:311px;height:311px;border-radius:50%}
.service-name{position:absolute;left:0;width:366px;font-family:"Roboto",sans-serif;font-size:21px;letter-spacing:.5px}
.service-text{position:absolute;left:33px;width:300px;font-size:13px;line-height:17px}
.service-btn{width:156px;height:39px;left:105px}

/* products */
.products-title{top:2750px;font-size:36px}
.price-list{position:absolute;left:112px;top:2866px;width:484px;list-style:none}
.price-list li{display:flex;align-items:center;height:36px;font-size:22px}
.item{font-style:italic;font-weight:600;color:#222}
.leader{flex:1;border-bottom:1px dashed #9a9a9a;margin:4px 12px 0}
.price{font-family:"Open Sans",sans-serif;color:var(--red);font-weight:400;font-size:21px}
.products-photo{left:667px;top:2832px;width:418px;height:418px;background:radial-gradient(circle at 50% 40%,#c49a3a 0%,#8a7a5a 35%,#6a5a48 65%,#4a3a2c 100%)}

/* contact */
.contact-title{top:3336px;font-size:29px;font-weight:500}
.field{position:absolute;background:var(--white);font-size:12px;color:#888;padding:0 10px;display:flex;align-items:center}
.field.msg{align-items:flex-start;padding-top:12px}
.send-btn{left:521px;top:3651px;width:154px;height:39px}

/* footer */
.site-footer{position:absolute;left:0;top:3776px;width:1200px;height:338px;background:var(--footer);color:var(--white)}
.site-footer .brand{top:138px}
.site-footer .brand-name{color:var(--white)}
.foot-col{position:absolute;top:92px;font-family:"Roboto",sans-serif}
.foot-col h4{font-size:12px;font-weight:500;margin-bottom:18px}
.foot-col li{list-style:none;font-size:13px;line-height:27px;color:#e6e6e6}
.contact-row{display:flex;align-items:center;gap:10px;font-size:12.5px;color:#e6e6e6;height:27px}
.foot-col p{font-size:13px;line-height:17px;color:#e6e6e6;width:260px}
.news-input{margin-top:12px;width:258px;height:36px;border-radius:18px;background:var(--white);color:#666;font-size:12px;display:flex;align-items:center;padding-left:16px}
.news-btn{position:relative;margin-top:8px;width:258px;height:36px;border-radius:18px;background:var(--red);display:flex;align-items:center;justify-content:center;font-size:12px}

.bottom-bar{position:absolute;left:0;top:4114px;width:1200px;height:61px;background:var(--paper)}
.copyright{position:absolute;left:73px;top:24px;font-size:12px;color:var(--ink);font-family:"Roboto",sans-serif}
.social{position:absolute;top:15px;display:flex;gap:10px;left:963px}
.social span{width:32px;height:32px;border-radius:50%;background:#333}
.social span:first-child{background:var(--red)}
</style>
</head>
<body>

<header class="site-header">
  <div class="brand"><span class="brand-mark"></span><span class="brand-name">HARROWFIELD LOAM<br>&amp; EXCAVATION</span></div>
  <div class="header-phone">
    <span class="phone-dot"><svg width="14" height="14" viewBox="0 0 24 24"><path fill="#fff" d="M6.6 10.8a15 15 0 006.6 6.6l2.2-2.2c.3-.3.7-.4 1-.2 1.1.4 2.3.6 3.6.6.6 0 1 .4 1 1V20c0 .6-.4 1-1 1A17 17 0 013 4c0-.6.4-1 1-1h3.5c.6 0 1 .4 1 1 0 1.3.2 2.5.6 3.6.1.3 0 .7-.2 1z"/></svg></span>
    703-555-0148
  </div>
  <div class="btn quote-btn">Get A Quote</div>
  <nav class="main-nav">
    <span class="active">HOME</span><span>ABOUT US</span><span>SERVICES</span><span>PRODUCTS/PRICING</span><span>CONTACT US</span>
  </nav>
</header>

<section class="hero" role="img" aria-label="Wheel loader working beside large topsoil piles at the yard">
  <h1 class="hero-title">Best Quality Topsoil For<br>The Best Results</h1>
  <div class="slide-dots"><span></span><span class="on"></span><span></span><span></span></div>
  <div class="slide-num">— 02</div>
</section>

<h2 class="section-title about-title">ABOUT US</h2>
<div class="title-rule"></div>
<div class="photo about-photo" role="img" aria-label="Yellow excavator and bulldozer on a red clay building site"></div>
<div class="about-text">
  <p>A leading Excavating Contractor in the NOVA area. I provide my clients with a comprehensive approach to contracting and specialize in a wide range of services. Ever since starting out as a professional Excavating Contractor,</p>
  <p>I've prioritized serving my clients' needs and satisfaction above everything else. I take care of all the small details so you don't have to. Get in touch to bring your vision to life today!</p>
  <p>Our emphasis is to produce the very best quality topsoil for the best results! Our topsoil and organics make quality ready-made soils and lawn amendments. We can custom blend any products which include leaf mulch, Verdaro compost and Brackens compost to make the perfect mixtures for your needs.</p>
</div>
<div class="btn about-btn">Read More</div>

<section class="services">
  <h2 class="section-title services-title">Our Services</h2>

  <div class="service-card" style="left:50px;top:170px;height:490px">
    <div class="service-clip" style="top:0"><div role="img" aria-label="Excavator on gravel among pine trees" style="background:radial-gradient(circle at 50% 45%,#d8a21f 0%,#4f7a3a 45%,#2f5a2a 80%,#8a8a84 100%)"></div></div>
    <div class="service-name" style="top:296px">EXCAVATION</div>
    <div class="service-text" style="top:337px">We provide a wide variety of excavation services, from residential to large commercial projects.</div>
    <div class="btn service-btn" style="top:399px">Read More</div>
  </div>

  <div class="service-card featured" style="left:418px;top:147px;height:485px">
    <div class="service-clip" style="top:23px"><div role="img" aria-label="Excavator demolishing an old house" style="background:radial-gradient(circle at 50% 50%,#8a7a60 0%,#5f7fb0 50%,#3a6fc0 100%)"></div></div>
    <div class="service-name" style="top:319px">DEMOLITION</div>
    <div class="service-text" style="top:360px">We specialize in demolition projects. From tearing down and removing an old home to clearing the site.</div>
    <div class="btn service-btn" style="top:422px">Read More</div>
  </div>

  <div class="service-card" style="left:780px;top:170px;height:490px">
    <div class="service-clip" style="top:0"><div role="img" aria-label="Screening machine on a dark topsoil pile" style="background:linear-gradient(180deg,#b9bcbf 0%,#9a9c9d 45%,#3a332c 60%,#2a241f 100%)"></div></div>
    <div class="service-name" style="top:296px">TOPSOIL</div>
    <div class="service-text" style="top:337px">Our emphasis is to produce the very best quality topsoil for the best results! Our topsoil and organics.</div>
    <div class="btn service-btn" style="top:399px">Read More</div>
  </div>

  <div class="service-card" style="left:50px;top:683px;height:490px">
    <div class="service-clip" style="top:0"><div role="img" aria-label="Large pile of hauled soil" style="background:linear-gradient(180deg,#c9cdd0 0%,#8a6a4a 35%,#6e4f35 60%,#b58a5a 100%)"></div></div>
    <div class="service-name" style="top:300px">HAULING</div>
    <div class="service-text" style="top:341px">Lorem Ipsum is simply dummy text of the printing and typesetting industry. Lorem Ipsum has been the industry's.</div>
    <div class="btn service-btn" style="top:399px">Read More</div>
  </div>

  <div class="service-card" style="left:418px;top:683px;height:490px">
    <div class="service-clip" style="top:0"><div role="img" aria-label="Land clearing with a burn pile in bare woods" style="background:radial-gradient(circle at 60% 65%,#d06a2a 0%,#7a6a5a 30%,#9a9590 70%,#b8b6b4 100%)"></div></div>
    <div class="service-name" style="top:300px">CLEARING</div>
    <div class="service-text" style="top:341px">Land clearing is the process of removing trees, stumps, brush, stones and other obstacles from an area as required</div>
    <div class="btn service-btn" style="top:399px">Read More</div>
  </div>

  <div class="service-card" style="left:780px;top:683px;height:490px">
    <div class="service-clip" style="top:0"><div role="img" aria-label="Bulldozer grading red clay near farm buildings" style="background:linear-gradient(180deg,#cfd8e2 0%,#bcc6cf 35%,#a9543a 55%,#b8523a 100%)"></div></div>
    <div class="service-name" style="top:300px">GRADING</div>
    <div class="service-text" style="top:341px">A type of excavation used to correct drainage issues, prepare the ground for home extensions, and for purely aesthetic purposes.</div>
    <div class="btn service-btn" style="top:399px">Read More</div>
  </div>
</section>

<h2 class="section-title products-title">PRODUCTS &amp; PRICING</h2>
<ul class="price-list">
  <li><span class="item">Unscreened Topsoil</span><span class="leader"></span><span class="price">$10</span></li>
  <li><span class="item">Shredded Topsoil</span><span class="leader"></span><span class="price">$14</span></li>
  <li><span class="item">Screened Topsoil</span><span class="leader"></span><span class="price">$20</span></li>
  <li><span class="item">Double Shredded Hardwood Mulch</span><span class="leader"></span><span class="price">$15</span></li>
  <li><span class="item">Brown Dyed Mulch</span><span class="leader"></span><span class="price">$28</span></li>
  <li><span class="item">Black Dyed Mulch</span><span class="leader"></span><span class="price">$28</span></li>
  <li><span class="item">Premium Leaf Compost</span><span class="leader"></span><span class="price">$27</span></li>
  <li><span class="item">Brackens Soil Builder</span><span class="leader"></span><span class="price">$34</span></li>
  <li><span class="item">Screened Topsoil &amp; ½ Leaf Mulch</span><span class="leader"></span><span class="price">$27</span></li>
  <li><span class="item">Screened Topsoil &amp; ½ Brackens</span><span class="leader"></span><span class="price">$34</span></li>
</ul>
<div class="photo products-photo" role="img" aria-label="Excavator with screening bucket working a soil pile"></div>

<h2 class="section-title contact-title">Quick Contact</h2>
<div class="field" style="left:344px;top:3416px;width:246px;height:60px">Name*</div>
<div class="field" style="left:344px;top:3485px;width:246px;height:60px">Phone*</div>
<div class="field" style="left:344px;top:3556px;width:246px;height:60px">Email*</div>
<div class="field msg" style="left:602px;top:3416px;width:243px;height:204px">Message</div>
<div class="btn send-btn">Send</div>

<footer class="site-footer">
  <div class="brand"><span class="brand-mark"></span><span class="brand-name">HARROWFIELD LOAM<br>&amp; EXCAVATION</span></div>
  <div class="foot-col" style="left:469px">
    <h4>QUICK LINKS</h4>
    <ul><li>&gt;&nbsp; Home</li><li>&gt;&nbsp; About us</li><li>&gt;&nbsp; Services</li><li>&gt;&nbsp; Products/Pricing</li><li>&gt;&nbsp; Contact us</li></ul>
  </div>
  <div class="foot-col" style="left:642px">
    <h4>CONTACT INFO</h4>
    <div class="contact-row"><svg width="12" height="12" viewBox="0 0 24 24"><path fill="#fff" d="M6.6 10.8a15 15 0 006.6 6.6l2.2-2.2c.3-.3.7-.4 1-.2 1.1.4 2.3.6 3.6.6.6 0 1 .4 1 1V20c0 .6-.4 1-1 1A17 17 0 013 4c0-.6.4-1 1-1h3.5c.6 0 1 .4 1 1 0 1.3.2 2.5.6 3.6.1.3 0 .7-.2 1z"/></svg>540-555-0162</div>
    <div class="contact-row"><svg width="13" height="10" viewBox="0 0 26 20"><rect x="1" y="1" width="24" height="18" fill="none" stroke="#fff" stroke-width="2"/><path d="M1 1l12 10L25 1" fill="none" stroke="#fff" stroke-width="2"/></svg>info@harrowfieldloam.com</div>
    <div class="contact-row" style="margin-top:20px"><svg width="12" height="14" viewBox="0 0 24 28"><path fill="#fff" d="M12 0a9 9 0 00-9 9c0 7 9 19 9 19s9-12 9-19a9 9 0 00-9-9zm0 13a4 4 0 110-8 4 4 0 010 8z"/></svg>2216 Quarry Bend Rd</div>
    <div class="contact-row" style="padding-left:22px">Elmridge, VA 20199</div>
  </div>
  <div class="foot-col" style="left:863px">
    <h4>NEWSLETTER</h4>
    <p>Lorem Ipsum is simply dummy text of printing and typesetting industry.</p>
    <div class="news-input">Email Address</div>
    <div class="news-btn">SUBSCRIBE</div>
  </div>
</footer>

<div class="bottom-bar">
  <div class="copyright">Copyright © 2021 <strong>HARROWFIELD</strong>. All Rights Reserved.</div>
  <div class="social"><span></span><span></span><span></span><span></span></div>
</div>

</body>
</html>
```